Kelvane Plumbing Business cards

Company is Kelvane Plumbing.
name Dashel Morrowby, I am a plumber, drainer, gasfitter and roofer
Mobile: 0431 906 154
Email address: info@kelvaneplumbing.example (check out my website for some ideas)
Website: www.kelvaneplumbing.example
ABN: 82 916 203 471
LIC: 604517K

I am reliable all round plumber. I am a 24 hour emergency service. Kelvane Plumbing is a professional plumbing service in the Illawarra, South Coast, Southern Sydney and Southern Highland regions of NSW. We offer a 24 hour emergency service for piece of mind to our customers. Call us now to see how we can help you. Kelvane Plumbing approaches every job with attention to detail and excellent customer service. With our superior workmanship you can be confident that the job will be done right the first time around. You can rest assured with results that are guaranteed to last.

Target Market(s)

the general public

Contact Information for Business Card

look up website for some ideas something with similar colours to logo and new modern and to catch the eye.

Colors
fdfdfd
ffffff
000000
7f7f7f
aaaaaa
33a6d7
0492cd

Requirements
Must have
• all contact details
• company- Kelvane Plumbing
• name- Dashel Morrowby
• number mobile- 0431 906 154
• Email address- info@kelvaneplumbing.example
• Website- www.kelvaneplumbing.example
• ABN- 82 916 203 471
• LIC- 604517K

```html
<!DOCTYPE html>
<html lang="en">
<head>
<meta charset="utf-8">
<title>Kelvane Plumbing Business Cards</title>
<link rel="stylesheet" href="https://fonts.googleapis.com/css2?family=Montserrat:wght@500;600;700&display=swap">
<style>
  :root {
    --page: #e9e9e9;
    --black: #1a1a1a;
    --white: #ffffff;
    --off-white: #fdfdfd;
    --grey: #7f7f7f;
    --light-grey: #aaaaaa;
    --blue: #33a6d7;
    --deep-blue: #0492cd;
    --dim: #3a3a3a;
  }
  * { margin: 0; padding: 0; box-sizing: border-box; }
  html, body { width: 1200px; height: 1200px; overflow: hidden; }
  body {
    background: var(--page);
    font-family: "Montserrat", Arial, sans-serif;
    display: flex;
    flex-direction: column;
    align-items: center;
    justify-content: center;
    gap: 60px;
  }
  .card {
    position: relative;
    width: 860px;
    height: 500px;
    overflow: hidden;
  }

  /* Back face */
  .card--back { background: var(--black); }
  .back-name {
    position: absolute;
    top: 180px;
    left: 0; right: 0;
    text-align: center;
    font-weight: 700;
    font-size: 64px;
    letter-spacing: 2px;
    color: var(--dim);
    text-transform: uppercase;
  }
  .back-web {
    position: absolute;
    left: 78px; right: 78px;
    top: 400px;
    height: 54px;
    border: 2px solid #555;
    border-radius: 27px;
    display: flex;
    align-items: center;
    justify-content: center;
    font-size: 19px;
    font-weight: 500;
    color: #4a4a4a;
  }

  /* Front face */
  .card--front { background: var(--white); }
  .front-name {
    position: absolute;
    left: 40px;
    top: 120px;
    font-weight: 700;
    font-size: 66px;
    letter-spacing: 1px;
    color: var(--deep-blue);
    text-transform: uppercase;
    line-height: 1;
  }
  .band {
    position: absolute;
    left: 0; right: 0;
    top: 275px;
    height: 58px;
    display: flex;
  }
  .band__blue {
    width: 700px;
    background: var(--deep-blue);
    display: flex;
    align-items: center;
    padding-left: 40px;
    color: var(--white);
    font-weight: 600;
    font-size: 30px;
  }
  .band__grey { flex: 1; background: var(--grey); }
  .band-mark {
    position: absolute;
    left: 700px;
    top: 264px;
    width: 80px;
    height: 80px;
    margin-left: -40px;
    border-radius: 50%;
    background: var(--white);
    border: 4px solid var(--deep-blue);
  }
  .contacts {
    position: absolute;
    left: 40px;
    top: 385px;
    list-style: none;
    font-size: 17px;
    font-weight: 500;
    color: #333;
  }
  .contacts li {
    display: flex;
    align-items: center;
    gap: 12px;
    height: 29px;
  }
  .contacts svg { width: 20px; height: 20px; fill: var(--deep-blue); }
  .registration {
    position: absolute;
    right: 40px;
    top: 413px;
    text-align: right;
    font-size: 19px;
    font-weight: 500;
    color: #333;
    line-height: 29px;
  }
  .registration b { color: var(--deep-blue); font-weight: 700; }
</style>
</head>
<body>
  <section class="card card--back">
    <div class="back-name">Kelvane Plumbing</div>
    <div class="back-web">www.kelvaneplumbing.example</div>
  </section>

  <section class="card card--front">
    <div class="front-name">Kelvane Plumbing</div>
    <div class="band">
      <div class="band__blue">Dashel Morrowby</div>
      <div class="band__grey"></div>
    </div>
    <div class="band-mark"></div>
    <ul class="contacts">
      <li>
        <svg viewBox="0 0 20 20" aria-hidden="true"><rect x="5" y="1" width="10" height="18" rx="2"/><rect x="7" y="3" width="6" height="11" fill="#fff"/></svg>
        0431 906 154
      </li>
      <li>
        <svg viewBox="0 0 20 20" aria-hidden="true"><rect x="1" y="4" width="18" height="12" rx="2"/><path d="M2 5l8 6 8-6" stroke="#fff" stroke-width="1.5" fill="none"/></svg>
        info@kelvaneplumbing.example
      </li>
      <li>
        <svg viewBox="0 0 20 20" aria-hidden="true"><circle cx="10" cy="10" r="9"/><path d="M1 10h18M10 1c-4 4-4 14 0 18M10 1c4 4 4 14 0 18" stroke="#fff" stroke-width="1.3" fill="none"/></svg>
        www.kelvaneplumbing.example
      </li>
    </ul>
    <div class="registration">
      <div><b>ABN:</b> 82 916 203 471</div>
      <div><b>LIC:</b> 604517K</div>
    </div>
  </section>
</body>
</html>
```